Vero-Shine Janitorial Services

Looking for a modern design for my new business. I like the clear see through of the card I've attached. The business is built around The Brightwell Omni 720 system, with that said I'd like to add the brightwell logo on the bachside with the statement of Powered by (then the Brightwell Logo). I really like the layout and color schemes of the card I attached. Black, Blue, and White. I would like to incorporate three images into the diamond shape, as seem in the layout.

Martin Okafor
Managing Partner

Still waiting on revisions?

```html
<!DOCTYPE html>
<html lang="en">
<head>
<meta charset="UTF-8">
<title>Vero-Shine Janitorial Services – Business Card</title>
<link href="https://fonts.googleapis.com/css2?family=Josefin+Slab:wght@600&family=Poppins:wght@400;500&display=swap" rel="stylesheet">
<style>
  :root {
    --ink: #0a0a0b;
    --paper: #ffffff;
    --sky: #1ea7ea;
    --royal: #1b6fd1;
    --stage: #e9ecef;
    --grey-text: #3a3d42;
    --muted: #6b7078;
  }
  * { margin: 0; padding: 0; box-sizing: border-box; }
  html, body { width: 1200px; height: 900px; overflow: hidden; }
  body {
    background: var(--stage);
    font-family: "Poppins", sans-serif;
    position: relative;
  }
  .card {
    position: absolute;
    left: 250px;
    width: 700px;
    height: 400px;
    overflow: hidden;
    box-shadow: 0 10px 30px rgba(0,0,0,0.18);
  }
  .card--front { top: 40px; background: var(--ink); }
  .card--back { top: 460px; background: var(--paper); }

  /* Front */
  .front-backdrop {
    position: absolute; inset: 0 0 14px 0;
    background: radial-gradient(ellipse at 30% 45%, #24272b 0%, #131518 60%, #0b0c0d 100%);
  }
  .front-title {
    position: absolute; left: 50px; top: 150px;
  }
  .brand-name {
    font-family: "Josefin Slab", serif;
    font-weight: 600;
    letter-spacing: 3px;
  }
  .front-title .brand-name { color: var(--paper); font-size: 64px; line-height: 1; }
  .front-title .tagline {
    color: var(--sky); font-family: "Josefin Slab", serif; font-weight: 600;
    font-size: 26px; letter-spacing: 3px; margin-top: 8px;
  }
  .photo-diamond {
    position: absolute;
    width: 100px; height: 100px;
    transform: translate(-50%, -50%) rotate(45deg);
    border: 3px solid var(--sky);
  }
  .photo-diamond--left {
    left: 490px; top: 193px;
    background: linear-gradient(135deg, #3b4148, #1c2024);
  }
  .photo-diamond--top {
    left: 570px; top: 113px;
    background: linear-gradient(135deg, #4a525b, #22272c);
  }
  .photo-diamond--bottom {
    left: 570px; top: 273px;
    background: linear-gradient(135deg, #2f353b, #15181b);
  }
  .edge-stripe {
    position: absolute; left: 0; right: 0; bottom: 0; height: 14px;
    background: var(--sky);
  }

  /* Back */
  .partner-mark {
    position: absolute; left: 44px; top: 38px;
    display: flex; align-items: center; gap: 10px;
  }
  .partner-mark .powered-by {
    color: var(--muted); font-size: 15px; font-weight: 400;
  }
  .partner-mark .partner-name {
    color: var(--royal); font-size: 22px; font-weight: 500;
  }
  .partner-mark .dot {
    width: 34px; height: 34px; border-radius: 50%;
    border: 3px solid var(--sky);
  }
  .client-mark {
    position: absolute; right: 48px; top: 78px;
    text-align: right;
  }
  .client-mark .seal {
    display: inline-block; width: 74px; height: 74px; border-radius: 50%;
    background: var(--sky); margin-bottom: 10px;
  }
  .client-mark .brand-name { color: var(--grey-text); font-size: 44px; line-height: 1; }
  .client-mark .tagline {
    color: var(--royal); font-family: "Josefin Slab", serif; font-weight: 600;
    font-size: 17px; letter-spacing: 1px; margin-top: 2px;
  }
  .person {
    position: absolute; left: 44px; top: 196px;
  }
  .person-name { color: var(--grey-text); font-size: 24px; letter-spacing: 1px; text-transform: uppercase; }
  .person-role { color: var(--royal); font-size: 17px; }
  .rule {
    position: absolute; left: 44px; right: 48px; top: 258px;
    height: 2px; background: var(--sky);
  }
  .contact-band {
    position: absolute; left: 0; right: 0; bottom: 14px; height: 100px;
    background: var(--ink);
    display: flex; align-items: center; justify-content: space-between;
    padding: 0 48px 0 44px;
    color: var(--paper); font-size: 16px;
  }
  .contact-list { list-style: none; line-height: 1.6; }
  .contact-list li { display: flex; align-items: center; gap: 10px; }
  .contact-list svg { width: 14px; height: 14px; flex: none; }
  .band-divider { width: 2px; height: 34px; background: var(--sky); }
  .web-accent { color: var(--sky); }
</style>
</head>
<body>

<section class="card card--front">
  <div class="front-backdrop"></div>
  <div class="front-title">
    <div class="brand-name">Vero-Shine</div>
    <div class="tagline">Janitorial Services</div>
  </div>
  <div class="photo-diamond photo-diamond--top" role="img" aria-label="Photo of a technician in protective gear disinfecting an office"></div>
  <div class="photo-diamond photo-diamond--left" role="img" aria-label="Photo of a freshly cleaned office interior"></div>
  <div class="photo-diamond photo-diamond--bottom" role="img" aria-label="Photo of electrostatic spray cleaning equipment"></div>
  <div class="edge-stripe"></div>
</section>

<section class="card card--back">
  <div class="partner-mark">
    <span class="powered-by">Powered by</span>
    <span class="dot"></span>
    <span class="partner-name">Brightwell</span>
  </div>

  <div class="client-mark">
    <span class="seal"></span>
    <div class="brand-name">Vero-Shine</div>
    <div class="tagline">Janitorial Services</div>
  </div>

  <div class="person">
    <div class="person-name">Martin Okafor</div>
    <div class="person-role">Managing Partner</div>
  </div>
  <div class="rule"></div>

  <div class="contact-band">
    <ul class="contact-list">
      <li>
        <svg viewBox="0 0 16 16"><path d="M2 5c0-2 3-3 6-3s6 1 6 3l-2 1-1-2H5L4 6zM4 7h8l2 6H2z" fill="var(--sky)"/></svg>
        555-014-2270
      </li>
      <li>
        <svg viewBox="0 0 16 16"><rect x="4" y="1" width="8" height="14" rx="1.5" fill="none" stroke="var(--sky)" stroke-width="2"/></svg>
        555-014-2270
      </li>
    </ul>
    <div class="band-divider"></div>
    <ul class="contact-list">
      <li>
        <svg viewBox="0 0 16 16"><rect x="1" y="3" width="14" height="10" fill="var(--sky)"/><path d="M1 3l7 6 7-6" fill="none" stroke="var(--ink)" stroke-width="1.5"/></svg>
        hello@veroshinemail.com
      </li>
      <li>
        <svg viewBox="0 0 16 16"><circle cx="8" cy="8" r="6.5" fill="none" stroke="var(--sky)" stroke-width="1.5"/><path d="M1.5 8h13M8 1.5c-3 3-3 10 0 13M8 1.5c3 3 3 10 0 13" fill="none" stroke="var(--sky)" stroke-width="1.2"/></svg>
        <span>www.<span class="web-accent">VEROSHINECO</span>.com</span>
      </li>
    </ul>
  </div>
  <div class="edge-stripe"></div>
</section>

</body>
</html>
```